依頼詳細
弊社サービスをご利用いただいてる会員様向けのデザインをお願いします。法人のように堅苦しい感じではなく、先進的で柔らかいイメージを希望します。
記載項目
KALVINO(サイト名)、住所、電話番号、FAX、HP
希望イメージ
シンプル 複雑
単色 カラフル
暗い 明るい
日常 高級
遊び心 厳粛
未来的 伝統的
女性的 男性的
希望する色
緑系、青系
補足説明
添付したロゴを使用して頂きたいです。
封筒の印刷面は部分印刷となります。
■ 選んだ理由

今回は会員の皆様に使用する封筒でしたので、温かい雰囲気があるデザインを選ばせて頂きました。

■ 提案者全員のお礼・コメント

みなさま、素敵なデザインのご提案をして頂きまして誠にありがとうございました。

```html
<!DOCTYPE html>
<html lang="ja">
<head>
<meta charset="UTF-8">
<title>KALVINO 会員様向け封筒</title>
<link rel="stylesheet" href="https://fonts.googleapis.com/css2?family=Montserrat:wght@500&family=Noto+Sans+JP:wght@400&display=swap">
<style>
  :root {
    --paper: #ffffff;
    --backdrop: #ffffff;
    --edge: #9a9a9a;
    --leaf-light: #c6deb2;
    --teal: #4f8a78;
    --text-light: #ffffff;
  }
  html, body {
    margin: 0;
    padding: 0;
    overflow: hidden;
    background: var(--backdrop);
  }
  .canvas {
    position: relative;
    width: 846px;
    height: 1200px;
    overflow: hidden;
    background: var(--backdrop);
  }
  .envelope-art {
    position: absolute;
    inset: 0;
  }
  .brand {
    position: absolute;
    left: 549px;
    top: 752px;
    width: 200px;
    text-align: center;
    color: var(--text-light);
  }
  .brand-mark {
    display: block;
    width: 104px;
    height: 104px;
    margin: 0 auto 26px;
    border: 5px solid var(--text-light);
    border-radius: 50%;
    box-sizing: border-box;
  }
  .brand-name {
    font-family: "Montserrat", sans-serif;
    font-weight: 500;
    font-size: 26px;
    letter-spacing: 9px;
    margin: 0;
    padding-left: 9px;
  }
  .contact {
    position: absolute;
    right: 118px;
    top: 1040px;
    margin: 0;
    text-align: right;
    color: var(--text-light);
    font-family: "Noto Sans JP", sans-serif;
    font-weight: 400;
    font-size: 12.5px;
    line-height: 25px;
    font-style: normal;
    letter-spacing: 0.5px;
  }
</style>
</head>
<body>
<main class="canvas">
  <svg class="envelope-art" width="846" height="1200" viewBox="0 0 846 1200" aria-hidden="true">
    <polygon class="flap" points="128,62 728,62 738,164 104,164" fill="var(--leaf-light)"/>
    <rect class="envelope-body" x="104" y="164" width="634" height="964" fill="var(--paper)"/>
    <polygon class="accent-band" points="437,164 738,164 738,1128 183,1128" fill="var(--leaf-light)"/>
    <polygon class="teal-panel" points="474,164 738,164 738,1128 282,1128" fill="var(--teal)"/>
    <rect class="envelope-outline" x="104.5" y="164.5" width="633" height="963" fill="none" stroke="var(--edge)" stroke-width="1"/>
  </svg>

  <div class="brand">
    <span class="brand-mark"></span>
    <p class="brand-name">KALVINO</p>
  </div>

  <address class="contact">
    〒000-0000　東京都緑ヶ丘市若葉町 1-234-567<br>
    TEL : 00-0000-0000　FAX : 00-0000-0000<br>
    www.kalvino-member.jp
  </address>
</main>
</body>
</html>
```